Contemporary Elegant Business Card Design for an International Trade Company in the Wine Industry

We need a new business card design for an international trade company in the wine and winemaking industry. The overall feel of the card should be contemporary, upscale, luxurious and elegant. It should communicate confidence and professionalism. The colors should complementary to our logo design (burgundy, gold, and black).
Inspiration: rich velvet tapestry
The card should include the following information:
Business: Brovenna Trading/Shipping, LLC.
Name: Marcus T. Hollenbrand
Title: CEO
Email: mark@brovennatrading.example
Phone: 555-294-6172
www.brovennatrading.example
Updates
Project Deadline Extended
Reason: We'd like the designers that we requested some additional designs from to still submit designs. Thank you!
Industry/Entity Type
Business
Contact Information for Business Card
Title: CEO
Phone: 555-294-6172
www.brovennatrading.example
Look and feel

```html
<!DOCTYPE html>
<html lang="en">
<head>
<meta charset="utf-8">
<title>Brovenna Trading/Shipping – Business Card</title>
<link rel="stylesheet" href="https://fonts.googleapis.com/css2?family=Cinzel:wght@600;700&family=Open+Sans:wght@400;600&display=swap">
<style>
  :root {
    --stage: #2a2622;
    --card-black: #0b0b0b;
    --gold: #d9a13a;
    --gold-deep: #b98427;
    --burgundy: #7a1a2a;
    --ink-splash: #4a3f27;
    --white: #f4f1ea;
  }
  html, body {
    margin: 0;
    width: 1200px;
    height: 913px;
    overflow: hidden;
    background: var(--stage);
  }
  .stage {
    width: 1200px;
    height: 913px;
    display: flex;
    align-items: center;
    justify-content: center;
    gap: 40px;
  }
  .card {
    position: relative;
    width: 540px;
    height: 309px;
    background: var(--card-black);
    overflow: hidden;
    box-shadow: 0 12px 30px rgba(0,0,0,.45);
  }

  /* Front */
  .gold-band {
    position: absolute;
    left: 56px;
    top: 98px;
    width: 92px;
    bottom: 0;
    background: linear-gradient(180deg, var(--gold) 0%, var(--gold-deep) 100%);
  }
  .emblem-square {
    position: absolute;
    left: 66px;
    top: 88px;
    width: 76px;
    height: 76px;
    background: var(--burgundy);
  }
  .front-brand {
    position: absolute;
    left: 158px;
    top: 62px;
    color: var(--gold);
    font-family: "Cinzel", serif;
    font-weight: 700;
    line-height: 1;
  }
  .front-brand .brand-name { font-size: 26px; letter-spacing: 1px; }
  .front-brand .brand-tag { font-size: 7.5px; letter-spacing: .5px; margin-top: 3px; }
  .splash {
    position: absolute;
    left: 290px;
    top: 20px;
    width: 190px;
    height: 150px;
    border-radius: 48% 52% 44% 56% / 55% 42% 58% 45%;
    background: radial-gradient(ellipse at 45% 45%, var(--ink-splash) 0%, rgba(74,63,39,.55) 60%, rgba(74,63,39,0) 100%);
  }
  .divider {
    position: absolute;
    left: 236px;
    right: 0;
    top: 150px;
    height: 1px;
    background: var(--gold);
  }
  .person {
    position: absolute;
    left: 236px;
    top: 160px;
  }
  .person-name {
    font-family: "Cinzel", serif;
    font-weight: 700;
    font-size: 17px;
    color: var(--gold);
    letter-spacing: .5px;
  }
  .person-title {
    font-family: "Open Sans", sans-serif;
    font-size: 10px;
    color: var(--white);
    margin-top: 1px;
  }
  .contacts {
    list-style: none;
    margin: 14px 0 0;
    padding: 0;
    font-family: "Open Sans", sans-serif;
    font-size: 11.5px;
    color: var(--gold);
  }
  .contacts li {
    display: flex;
    align-items: center;
    gap: 8px;
    line-height: 19px;
  }
  .contacts svg { width: 9px; height: 9px; fill: none; stroke: var(--white); stroke-width: 1.3; }

  /* Back */
  .map-panel {
    position: absolute;
    left: 170px;
    top: 44px;
    width: 200px;
    height: 150px;
  }
  .map-field {
    position: absolute;
    inset: 0;
    background: linear-gradient(135deg, #c9a45f 0%, #a97a3c 55%, #d4b274 100%);
  }
  .back-square {
    position: absolute;
    left: 248px;
    top: 112px;
    width: 44px;
    height: 44px;
    background: var(--burgundy);
  }
  .back-brand {
    position: absolute;
    left: 0;
    right: 0;
    top: 202px;
    text-align: center;
    color: var(--white);
    font-family: "Cinzel", serif;
    font-weight: 700;
    line-height: 1;
  }
  .back-brand .brand-name { font-size: 34px; letter-spacing: 2px; }
  .back-brand .brand-tag { font-size: 9px; letter-spacing: .6px; margin-top: 4px; }
</style>
</head>
<body>
<main class="stage">

  <section class="card card-front" aria-label="Business card front">
    <div class="splash" role="img" aria-label="Soft golden-brown paint splash decoration"></div>
    <div class="gold-band"></div>
    <div class="emblem-square"></div>
    <div class="front-brand">
      <div class="brand-name">BROVENNA</div>
      <div class="brand-tag">TRADING AND SHIPPING</div>
    </div>
    <div class="divider"></div>
    <div class="person">
      <div class="person-name">MARCUS T. HOLLENBRAND</div>
      <div class="person-title">CEO</div>
      <ul class="contacts">
        <li>
          <svg viewBox="0 0 10 10"><path d="M2 1 L4 1 L4.6 3.2 L3.4 4 Q4.4 6 6 6.6 L6.8 5.4 L9 6 L9 8 Q5 9 1.6 5 Q1 3 2 1 Z"/></svg>
          <span>555-294-6172</span>
        </li>
        <li>
          <svg viewBox="0 0 10 10"><rect x="1" y="2.2" width="8" height="5.6"/><path d="M1 2.2 L5 5.4 L9 2.2"/></svg>
          <span>mark@brovennatrading.example</span>
        </li>
        <li>
          <svg viewBox="0 0 10 10"><circle cx="5" cy="5" r="4"/><path d="M1 5 H9 M5 1 Q2.5 5 5 9 M5 1 Q7.5 5 5 9"/></svg>
          <span>www.brovennatrading.example</span>
        </li>
      </ul>
    </div>
  </section>

  <section class="card card-back" aria-label="Business card back">
    <div class="map-panel">
      <div class="map-field" role="img" aria-label="Aged parchment world map"></div>
    </div>
    <div class="back-square"></div>
    <div class="back-brand">
      <div class="brand-name">BROVENNA</div>
      <div class="brand-tag">TRADING AND SHIPPING</div>
    </div>
  </section>

</main>
</body>
</html>
```